Game, Voice & Dedicated Server Company Needs a Business Card Design

We need a new business card design, centered around our new logo (PSD provided below).

Designs that we do like:
https://pixelmarsh.net/item/corporate-business-card/5382017?s_rank=43 (needs to be made more eye catching)

Our main areas of business are:
- Dedicated Servers
- Game Servers
- Voice Servers
- Mitigation Security Specialists

Industry/Entity Type

Business

Contact Information for Business Card

On the card: (and anything else you would suggest)
- Staff member name
- Staff member position in company
- Staff member phone number
- Staff member email
- Other / Staff member Skype
- Website link

Colors
9bcb3c
abd036

Requirements
Must have
• Design of Card:
• - Green (same green as the logo)
• - Business / Corporate design
• - Something a little different / abstract that shouts premium

```html
<!DOCTYPE html>
<html lang="en">
<head>
<meta charset="utf-8">
<title>Brightpath Hosting – Business Card</title>
<link rel="stylesheet" href="https://fonts.googleapis.com/css2?family=Arimo:wght@400;700&display=swap">
<style>
  :root {
    --green: #9bcb3c;
    --green-deep: #8cc63f;
    --grey-text: #8a8a8c;
    --grey-dark: #6d6e71;
    --card: #ffffff;
    --backdrop: #e4e4e6;
  }
  * { box-sizing: border-box; margin: 0; padding: 0; }
  html, body {
    width: 1200px; height: 800px; overflow: hidden;
    background: var(--backdrop);
    font-family: "Arimo", Arial, sans-serif;
  }
  .stage {
    width: 1200px; height: 800px;
    display: flex; align-items: center; justify-content: center; gap: 50px;
  }
  .card {
    position: relative;
    width: 525px; height: 300px;
    background: var(--card);
    box-shadow: 0 6px 18px rgba(0,0,0,.18);
    overflow: hidden;
  }
  /* front */
  .front .edge {
    position: absolute; width: 7px; background: var(--green); border-radius: 4px;
  }
  .front .edge-left { left: 0; top: 10px; height: 210px; }
  .front .edge-right { right: 0; bottom: 10px; height: 210px; }
  .brand {
    position: absolute;
    display: flex; align-items: center; gap: 16px;
  }
  .front .brand { left: 70px; top: 96px; }
  .brand-mark {
    width: 66px; height: 66px; background: var(--green);
  }
  .brand-name {
    color: var(--green);
    font-weight: 700;
    text-transform: uppercase;
    line-height: .95;
    letter-spacing: -1px;
  }
  .front .brand-name { font-size: 44px; }
  /* back */
  .back .edge {
    position: absolute; left: 0; right: 0; height: 7px; background: var(--green);
  }
  .back .edge-top { top: 0; }
  .back .edge-bottom { bottom: 0; }
  .back .brand { right: 34px; top: 46px; gap: 12px; }
  .back .brand-mark { width: 44px; height: 44px; }
  .back .brand-name { font-size: 30px; }
  .person {
    position: absolute; left: 34px; top: 168px;
  }
  .person-name {
    color: var(--green); font-weight: 700; font-size: 21px; letter-spacing: .3px;
  }
  .person-role {
    color: var(--grey-text); font-size: 17px; margin-top: 2px; letter-spacing: .3px;
  }
  .contacts {
    position: absolute; left: 258px; top: 150px;
    list-style: none;
    display: flex; flex-direction: column; gap: 7px;
  }
  .contacts li {
    display: flex; align-items: center; gap: 9px;
    color: var(--grey-text); font-size: 14.5px;
  }
  .contacts svg { width: 21px; height: 21px; flex: none; }
</style>
</head>
<body>
<main class="stage">
  <section class="card front" aria-label="Card front">
    <span class="edge edge-left"></span>
    <span class="edge edge-right"></span>
    <div class="brand">
      <span class="brand-mark"></span>
      <span class="brand-name">Brightpath<br>Hosting</span>
    </div>
  </section>

  <section class="card back" aria-label="Card back">
    <span class="edge edge-top"></span>
    <span class="edge edge-bottom"></span>
    <div class="brand">
      <span class="brand-mark"></span>
      <span class="brand-name">Brightpath<br>Hosting</span>
    </div>
    <div class="person">
      <p class="person-name">YOUR NAME</p>
      <p class="person-role">POSITIONS</p>
    </div>
    <ul class="contacts">
      <li>
        <svg viewBox="0 0 22 22" aria-hidden="true"><rect width="22" height="22" rx="4" fill="#9bcb3c"/><path d="M7.5 5.5l2 2.2-1.2 1.6c.8 1.7 2 2.9 3.6 3.7l1.6-1.2 2.2 2-1.2 2c-4.5-.4-8.3-4.2-8.6-8.7z" fill="#fff"/></svg>
        000 111 222
      </li>
      <li>
        <svg viewBox="0 0 22 22" aria-hidden="true"><rect width="22" height="22" rx="4" fill="#9bcb3c"/><rect x="5" y="7" width="12" height="8.5" fill="none" stroke="#fff" stroke-width="1.5"/><path d="M5 7l6 5 6-5" fill="none" stroke="#fff" stroke-width="1.5"/></svg>
        email@brightpathhosting.com
      </li>
      <li>
        <svg viewBox="0 0 22 22" aria-hidden="true"><rect width="22" height="22" rx="4" fill="#9bcb3c"/><path d="M5 6.5h12v7.5H10l-3 2.5V14H5z" fill="none" stroke="#fff" stroke-width="1.5" stroke-linejoin="round"/></svg>
        brightpathhosting
      </li>
      <li>
        <svg viewBox="0 0 22 22" aria-hidden="true"><rect width="22" height="22" rx="4" fill="#9bcb3c"/><circle cx="11" cy="11" r="6" fill="none" stroke="#fff" stroke-width="1.4"/><ellipse cx="11" cy="11" rx="2.6" ry="6" fill="none" stroke="#fff" stroke-width="1.2"/><path d="M5 11h12" stroke="#fff" stroke-width="1.2"/></svg>
        brightpathhosting.com
      </li>
    </ul>
  </section>
</main>
</body>
</html>
```